Golden Porch Living postcard

Golden Porch Living ®Our mission is to help our client’s to continue living in their own homes safely, independently, and comfortably as they age. Our team is comprised of Certified Aging in Place specialists, Universal Design Consultants, Registered Nurses and Certified Home Inspectors. We utilize our skills and training to assess, design and optimize our client’s homes to handle whatever physical challenges the future may bring, allowing them to remain where they want to be as they age…..at home!New company! We need a postcard for a direct mail campaign to help us launch. We understand all of the copy included in the attached document may not fit on the postcard. Demo is 55+ I know what you are thinking, where is the log? We don't have one. Long story short, in the past we have spent WAY too much time and EFFORT milling over a logo. SO...this time we found a font within Microsoft Word and applied it to our name and like it. Take a look at the uploaded document. Feel free to play with it a little...

Target Market(s)

55+ with a slight slant toward females viewer.

Font styles to use
Serif

Colors
85acd3
0355a3
ffffff

Requirements
Must have
• 1. statistics section-grab their attention
• 2. our mission statement- the goal
Nice to have
• 1. How we can help section
• Senior Services Industry

```html
<!DOCTYPE html>
<html lang="en">
<head>
<meta charset="utf-8">
<title>Golden Porch Living postcard</title>
<link href="https://fonts.googleapis.com/css2?family=Lato:ital,wght@0,400;0,700;0,900;1,400;1,700&family=Roboto+Condensed:wght@400;700&display=swap" rel="stylesheet">
<style>
:root{
  --bg:#8c6a47;
  --blue-deep:#0355a3;
  --blue-mid:#1c6cc0;
  --blue-light:#85acd3;
  --blue-pale:#a9c6e4;
  --white:#ffffff;
  --ink:#1d2a38;
  --navy:#14355f;
  --shadow:rgba(0,0,0,.35);
}
*{box-sizing:border-box;margin:0;padding:0}
html,body{width:907px;height:1200px;overflow:hidden}
body{background:var(--bg);font-family:'Lato',sans-serif;position:relative;color:var(--ink)}
.card{position:absolute;box-shadow:0 4px 10px var(--shadow);overflow:hidden}
.front{left:57px;top:65px;width:789px;height:510px;background:var(--white)}
.back{left:57px;top:626px;width:791px;height:512px;background:var(--white)}

/* front */
.top-band{position:absolute;left:0;top:0;width:100%;height:20px;background:linear-gradient(90deg,var(--blue-pale),var(--blue-light))}
.bottom-band{position:absolute;left:0;bottom:0;width:100%;height:40px;background:linear-gradient(90deg,var(--blue-light),var(--blue-pale),var(--blue-light));text-align:center;font-weight:700;letter-spacing:4.5px;font-size:14px;line-height:40px;color:var(--navy)}
.intro{position:absolute;left:0;top:20px;width:383px;height:450px;background:var(--white)}
.brand{position:absolute;left:22px;top:8px;font-size:30px;font-weight:700;color:var(--blue-deep);white-space:nowrap}
.tagline{position:absolute;right:12px;top:44px;font-size:17px;color:#111}
.photo{position:absolute;left:0;top:72px;width:383px;height:196px;background:linear-gradient(135deg,#8aa86b 0%,#c9d3c7 45%,#e4dfd6 70%,#b9c6a4 100%)}
.photo-rule{position:absolute;left:0;top:265px;width:383px;height:4px;background:var(--blue-deep)}
.headline{position:absolute;left:25px;top:272px;font-family:'Roboto Condensed',sans-serif;font-size:27px;color:#111}
.subhead{position:absolute;left:25px;top:306px;font-family:'Roboto Condensed',sans-serif;font-weight:700;font-size:12.5px;line-height:14px;color:var(--blue-deep);text-transform:uppercase}
.questions{position:absolute;left:25px;top:345px;width:350px;list-style:none;font-style:italic;font-weight:700;font-size:11px;line-height:14.5px;color:#1a1a1a}
.questions li{position:relative;padding-left:17px;margin-bottom:5px}
.questions li::before,.dots li::before{content:"";position:absolute;left:0;top:4px;width:7px;height:7px;border-radius:50%;background:currentColor}
.questions li::before{background:var(--blue-deep)}
.story{position:absolute;left:383px;top:20px;width:406px;height:450px;background:linear-gradient(180deg,var(--blue-deep),var(--blue-mid) 55%,var(--blue-deep));color:var(--white)}
.quote{position:absolute;left:18px;top:12px;width:376px;font-size:12.5px;line-height:15px;text-align:justify}
.quote b{font-weight:700}
.quote small{font-size:10.5px}
.pill{position:absolute;background:var(--white);color:#111;font-weight:700;border-radius:12px 0 0 12px;padding:0 12px}
.mission-pill{right:0;top:91px;width:135px;height:24px;font-size:15px;line-height:24px}
.mission{position:absolute;left:12px;top:130px;width:382px;font-size:12.3px;line-height:15.2px;text-align:justify}
.ask-pill{right:0;top:259px;width:135px;height:24px;font-size:15px;line-height:24px}
.dots{position:absolute;left:14px;top:292px;width:380px;list-style:none;font-size:12.3px;line-height:15.2px}
.dots li{position:relative;padding-left:18px;margin-bottom:5px}

/* back */
.offer{position:absolute;left:0;top:0;width:516px;height:424px;background:linear-gradient(180deg,var(--blue-deep),var(--blue-mid) 50%,var(--blue-deep));color:var(--white)}
.offer-pill{position:absolute;left:0;top:12px;width:391px;height:26px;background:var(--white);color:#111;font-weight:700;font-size:16px;line-height:26px;padding-left:19px;border-radius:0 13px 13px 0}
.offer h3{position:absolute;left:19px;font-style:italic;font-weight:700;font-size:13.5px}
.offer ul{position:absolute;left:18px;width:490px;list-style:none;font-size:12.2px;line-height:15px}
.offer li{position:relative;padding-left:19px;margin-bottom:4px}
.offer li::before{content:"";position:absolute;left:0;top:4px;width:7px;height:7px;border-radius:50%;background:var(--white)}
.contact-band{position:absolute;left:0;top:424px;width:516px;height:88px;background:linear-gradient(180deg,var(--blue-light),var(--blue-pale))}
.contact-tab{position:absolute;left:189px;top:410px;width:108px;height:24px;background:#1a1a1a;color:var(--white);font-weight:700;font-size:14px;line-height:24px;text-align:center}
.phone{position:absolute;left:0;top:447px;width:252px;height:38px;background:linear-gradient(180deg,var(--white),#dfe6ee);border-radius:0 19px 19px 0;display:flex;align-items:center;padding-left:22px;gap:12px;font-weight:700;font-size:26px;color:#111}
.phone svg{width:15px;height:15px}
.sign-brand{position:absolute;left:283px;top:444px;font-size:20px;font-weight:700;color:var(--blue-deep);white-space:nowrap}
.sign-rule{position:absolute;left:281px;top:470px;width:214px;height:1px;background:var(--white)}
.sign-url{position:absolute;left:283px;top:472px;font-size:14px;color:#111}
.divider{position:absolute;left:516px;top:0;width:9px;height:512px;background:var(--blue-light)}
.stamp{position:absolute;left:686px;top:21px;width:86px;height:101px;border:1px solid #555}
.address-line{position:absolute;left:541px;width:232px;height:1px;background:#555}
</style>
</head>
<body>

<section class="card front">
  <div class="top-band"></div>

  <div class="intro">
    <div class="brand">Golden Porch Living ®</div>
    <div class="tagline">Because you deserve it!</div>
    <div class="photo" role="img" aria-label="Photo of a smiling senior couple in front of their house"></div>
    <div class="photo-rule"></div>
    <h2 class="headline">As the 55+ generation ages</h2>
    <p class="subhead">They have many important questions to consider,<br>but may be none more important than these</p>
    <ul class="questions">
      <li>Once our physical abilities make living in our home, as it is today, a struggle, what are we going to do?</li>
      <li>Are we planning to move into an assisted living facility when our health declines? What will that cost?</li>
      <li>If we decide we want to stay in our home as we age is there someone who can help us design and build what we need?</li>
    </ul>
  </div>

  <div class="story">
    <p class="quote">❝ <b>Aging in place</b> has become the preferred lifestyle and a lower cost alternative to institutionalization. Experts expect home modifications, increased connectivity and improved healthcare will make this the obvious<br><small>lifestyle choice ❞</small></p>
    <div class="pill mission-pill">Our Mission</div>
    <p class="mission">Our mission is to help our client’s to continue living in their own homes safely, independently, and comfortably as they age. Our team is comprised of Certified Aging in Place specialists, Universal Design Consultants, Registered Nurses and Certified Home Inspectors. We utilize our skills and training to assess, design and optimize our client’s homes to handle whatever physical challenges the future may bring, allowing them to remain where they want to be as they age…..at home!</p>
    <div class="pill ask-pill">Ask yourself…</div>
    <ul class="dots">
      <li>Is your home functioning safely and efficiently? How do you know?</li>
      <li>Is your home well suited for the physical challenges that may come with natural aging or an unfortunate diagnosis?</li>
      <li>Are you aware there are many simple, cost effective and attractive ways to modify your home to make it fit your needs now and in the future?</li>
      <li>Are you aware there are many new technology products that can help make your home safe, functional and more enjoyable?</li>
    </ul>
  </div>

  <div class="bottom-band">www.goldenporchliving.com</div>
</section>

<section class="card back">
  <div class="offer">
    <div class="offer-pill">Free 30-minute in-home consultation includes…</div>
    <h3 style="top:52px">Free 30 minute in-home consultation</h3>
    <ul style="top:76px">
      <li>Registers you for free access to our network of pre-screened and senior friendly contractors and service providers</li>
      <li>Contractor fraud education literature made available for those who wish to DIY.</li>
      <li>Cost comparison between investing in your home vs. cost of an assisted living facility.</li>
    </ul>
    <h3 style="top:166px">Home Audit</h3>
    <ul style="top:190px">
      <li>Perform a comprehensive home inspection by certified inspector to assess the safety and functionality of your home.</li>
      <li>Identify what, if anything, needs to be addresses and refer the best contractor for the job.</li>
    </ul>
    <h3 style="top:266px">Aging in place consultation:</h3>
    <ul style="top:296px">
      <li>Produce a written “road map” identifying improvements that can be done to proatively address your physical needs now and in the future.</li>
      <li>Consult with one of our CCM certified nurses about anticipated physical restrictions based on any current medical conditions or concerns.</li>
      <li>Present and suggest home technology options that may be useful. Refer the appropriate contractors or product suppliers in our network to the homeowner.</li>
    </ul>
  </div>

  <div class="contact-band"></div>
  <div class="contact-tab">Contact Us</div>
  <div class="phone">
    <svg viewBox="0 0 24 24" aria-hidden="true"><path fill="#1a3a66" d="M6.6 10.8a15 15 0 0 0 6.6 6.6l2.2-2.2a1 1 0 0 1 1-.25 11.4 11.4 0 0 0 3.6.57 1 1 0 0 1 1 1V20a1 1 0 0 1-1 1A17 17 0 0 1 3 4a1 1 0 0 1 1-1h3.5a1 1 0 0 1 1 1c0 1.25.2 2.45.57 3.57a1 1 0 0 1-.25 1z"/></svg>
    0198765432
  </div>
  <div class="sign-brand">Golden Porch Living ®</div>
  <div class="sign-rule"></div>
  <div class="sign-url">www.goldenporchliving.com</div>

  <div class="divider"></div>
  <div class="stamp"></div>
  <div class="address-line" style="top:235px"></div>
  <div class="address-line" style="top:276px"></div>
  <div class="address-line" style="top:309px"></div>
</section>

</body>
</html>
```